Business card for a new cabinet shop company named Torvane Cabinets for high end cabinets

Design a business card, thinking dark rich green with colours to speak of high end luxury ie; cream, gold, black possibly

Miles Harwick
Director Craftsman
Email: info@torvanecabinets.com.au
Instagram : @torvane.cabinets

```html
<!DOCTYPE html>
<html lang="en">
<head>
<meta charset="utf-8">
<title>Torvane Cabinets – Business Card</title>
<link href="https://fonts.googleapis.com/css2?family=Poppins:wght@300;400;700&display=swap" rel="stylesheet">
<style>
  :root {
    --backdrop: #eceeee;
    --card: #252525;
    --card-back: #222322;
    --pattern-tone: #2c2d2c;
    --green: #2f6a45;
    --white: #ffffff;
  }
  * { margin: 0; padding: 0; box-sizing: border-box; }
  html, body {
    width: 1200px; height: 1108px; overflow: hidden;
    background: var(--backdrop);
    font-family: "Poppins", sans-serif;
  }
  .card {
    position: absolute;
    background: var(--card);
    color: var(--white);
  }
  .card-front { left: 219px; top: 50px; width: 775px; height: 473px; }
  .card-back  { left: 217px; top: 568px; width: 777px; height: 457px; background: var(--card-back); }

  .brand { position: absolute; display: flex; align-items: center; color: var(--green); font-weight: 400; }
  .brand-mark { background: var(--green); flex: none; }
  .brand-name { display: flex; flex-direction: column; line-height: 1; }
  .brand-word { letter-spacing: 1px; }
  .brand-sub { letter-spacing: 0.42em; }

  .front-brand { left: 112px; top: 72px; gap: 34px; }
  .front-brand .brand-mark { width: 120px; height: 120px; }
  .front-brand .brand-word { font-size: 88px; }
  .front-brand .brand-sub { font-size: 44px; margin-top: 14px; }

  .person { position: absolute; right: 402px; top: 318px; text-align: right; }
  .person-name { font-size: 30px; font-weight: 700; letter-spacing: 0.2px; }
  .person-role { font-size: 17px; font-weight: 300; margin-top: 2px; }

  .divider { position: absolute; left: 388px; top: 312px; width: 2px; height: 84px; background: var(--green); }

  .contact { position: absolute; left: 400px; top: 308px; font-weight: 300; }
  .contact-row { display: flex; align-items: center; gap: 10px; font-size: 18px; height: 29px; }
  .contact-icon { width: 16px; height: 16px; flex: none; }
  .contact-location { font-size: 21px; margin-top: 6px; }

  .back-pattern { position: absolute; inset: 0; background: linear-gradient(135deg, var(--card-back), var(--pattern-tone)); }
  .back-brand { left: 448px; top: 320px; gap: 18px; }
  .back-brand .brand-mark { width: 70px; height: 70px; }
  .back-brand .brand-word { font-size: 42px; }
  .back-brand .brand-sub { font-size: 20px; margin-top: 6px; }
</style>
</head>
<body>
  <section class="card card-front">
    <div class="brand front-brand">
      <span class="brand-mark"></span>
      <div class="brand-name">
        <span class="brand-word">Torvane</span>
        <span class="brand-sub">CABINETS</span>
      </div>
    </div>

    <div class="person">
      <p class="person-name">Miles Harwick</p>
      <p class="person-role">Director Craftsman</p>
    </div>

    <div class="divider"></div>

    <div class="contact">
      <p class="contact-row">
        <svg class="contact-icon" viewBox="0 0 16 16" aria-hidden="true">
          <rect x="1" y="3" width="14" height="10" fill="#2f6a45"/>
          <path d="M1 3 L8 9 L15 3" fill="none" stroke="#252525" stroke-width="1.4"/>
        </svg>
        info@torvanecabinets.com.au
      </p>
      <p class="contact-row">
        <svg class="contact-icon" viewBox="0 0 16 16" aria-hidden="true">
          <circle cx="8" cy="8" r="7.5" fill="#2f6a45"/>
        </svg>
        @torvane.cabinets
      </p>
      <p class="contact-location">Western Australia</p>
    </div>
  </section>

  <section class="card card-back">
    <div class="back-pattern" role="img" aria-label="Repeating brand pattern in faint charcoal tones"></div>
    <div class="brand back-brand">
      <span class="brand-mark"></span>
      <div class="brand-name">
        <span class="brand-word">Torvane</span>
        <span class="brand-sub">CABINETS</span>
      </div>
    </div>
  </section>
</body>
</html>
```